Homepage design

Hi
I m workingon hosting my website tallowbrisk.net on wordpress but the new design for the homepage is not good
I need a design just for that page on how to organise things and what to put there

```html
<!DOCTYPE html>
<html lang="en">
<head>
<meta charset="utf-8">
<title>Tallow Brisk – Money Exchange &amp; Transfers</title>
<link href="https://fonts.googleapis.com/css2?family=Ubuntu:wght@300;400;500;700&display=swap" rel="stylesheet">
<style>
:root{
  --navy:#17386a;
  --navy-dark:#0f2a52;
  --footer:#17345f;
  --footer-base:#10284b;
  --blue:#2b8bd6;
  --nav-top:#2f639b;
  --nav-bottom:#1d4476;
  --link:#3b90dc;
  --green:#7dbb1f;
  --red:#e3141a;
  --panel:#f0f0f0;
  --page:#efefef;
  --text:#555;
  --heading:#1b3358;
  --white:#fff;
}
*{box-sizing:border-box;margin:0;padding:0}
html,body{width:698px;height:1200px;overflow:hidden}
body{position:relative;font-family:"Ubuntu",sans-serif;color:var(--text);background:var(--white)}
.abs{position:absolute}
.top-band{left:0;top:0;width:698px;height:355px;background:var(--page)}
.brand{left:74px;top:14px;display:flex;align-items:center;gap:6px}
.brand-dot{width:12px;height:12px;border-radius:50%;background:var(--red)}
.brand-name{font-weight:700;font-size:17px;color:var(--navy)}
.brand-tag{left:92px;top:36px;font-size:5px;font-weight:700;color:var(--navy);letter-spacing:.2px}
.top-links{left:526px;top:10px;font-size:7px;color:#888;display:flex;gap:6px;align-items:center}
.lang-box{width:12px;height:8px;background:#1f3f86}
.top-phone{left:522px;top:36px;font-size:11.5px;color:#444}
.main-nav{left:70px;top:60px;width:558px;height:41px;background:linear-gradient(var(--nav-top),var(--nav-bottom));border-radius:2px;display:flex;align-items:center;padding-left:23px;font-size:9.5px;font-weight:500;color:var(--white)}
.main-nav span.sep{margin:0 13px;opacity:.8}
.hero{left:70px;top:108px;width:558px;height:220px;background:var(--white);box-shadow:0 0 3px rgba(0,0,0,.15)}
.hero-photo{left:3px;top:3px;width:372px;height:214px;background:linear-gradient(135deg,#4a5563 0%,#7c8591 40%,#e9d3cf 60%,#f0f0f0 100%)}
.hero-dots{left:10px;top:202px;display:flex;gap:3px}
.hero-dots i{width:8px;height:8px;border-radius:50%;background:var(--navy-dark)}
.quote-panel{left:375px;top:3px;width:180px;height:214px;background:var(--navy);padding:11px 14px}
.quote-panel h2{font-size:10.5px;font-weight:500;color:var(--white);margin-bottom:7px}
.field{width:153px;height:19px;border:1px solid #2c5289;background:#153463;font-size:6.5px;color:#6d84a6;padding:5px 3px;margin-bottom:6px}
.captcha{width:132px;height:50px;margin:6px 0 0 12px;background:#c91a1e;border-radius:3px;padding:3px}
.captcha-inner{width:100%;height:100%;background:#f3efe4;border-radius:2px}
.quote-btn{width:80px;height:18px;margin:8px 0 0 36px;background:var(--blue);color:var(--white);font-size:8px;text-align:center;line-height:18px}
h3.section{font-size:11px;font-weight:500;color:var(--heading)}
.welcome-h{left:73px;top:378px}
.copy{font-size:6.5px;line-height:14px;color:var(--text)}
.welcome-p1{left:73px;top:409px;width:365px}
.welcome-p2{left:73px;top:492px;width:365px}
.copy a{color:var(--blue);text-decoration:none}
.open-account{left:447px;top:375px;width:175px;height:42px;background:var(--blue);color:var(--white)}
.open-account b{position:absolute;left:51px;top:6px;font-size:13.5px;font-weight:500}
.open-account small{position:absolute;left:62px;top:26px;font-size:7px;color:#d5e9f8}
.safety{left:447px;top:429px;width:175px;height:87px;background:var(--navy)}
.safety-strip{left:0;top:0;width:37px;height:87px;background:var(--green)}
.safety h4{position:absolute;left:60px;top:11px;font-size:10.5px;font-weight:500;color:var(--white)}
.safety ul{position:absolute;left:44px;top:33px;list-style:none;font-size:7.5px;color:var(--white);line-height:15px}
.safety li{display:flex;gap:6px;align-items:center}
.card{top:549px;width:174px;height:193px;background:var(--panel);padding:9px 6px}
.card h3{font-size:10.5px;font-weight:500;color:var(--heading);line-height:16px;margin-bottom:14px}
.card .copy{font-size:6.3px;line-height:12.8px}
.card .btns{position:absolute;left:6px;top:154px;display:flex;gap:3px}
.btn{height:22px;padding:0 6px;font-size:7.5px;font-weight:500;color:var(--white);display:flex;align-items:center;gap:4px}
.btn.know{background:var(--blue)}
.btn.how{background:var(--navy-dark)}
.btn i{width:6px;height:6px;border-radius:50%;background:var(--white)}
.news{left:77px;top:760px;width:170px}
.news h4{font-size:7.5px;font-weight:700;color:#222;margin:14px 0 4px -1px}
.news .date{font-size:7.5px;color:#444;margin-bottom:4px}
.news p{font-size:6.3px;line-height:12.5px;color:#444}
.video-h{left:261px;top:760px}
.video{left:262px;top:786px;width:174px;height:105px;background:linear-gradient(#1f3450,#3b4d63 45%,#c58a3a 75%,#1d2a3d)}
.video-bar{left:262px;top:878px;width:174px;height:13px;background:#18263a}
.video-play{left:342px;top:833px}
.video-p{left:260px;top:905px;width:178px;text-align:center;font-size:6.3px;line-height:12px}
.download{left:447px;top:759px;width:175px;height:174px;background:var(--red);color:var(--white)}
.download b{position:absolute;left:14px;top:7px;font-size:11px;font-weight:500}
.download small{position:absolute;left:14px;top:23px;font-size:7.5px;color:#fbd}
.phones{left:28px;top:39px;width:118px;height:100px;background:linear-gradient(#3a3a3a,#222);border-radius:6px}
.store{top:142px;height:21px;font-size:7px;font-weight:500;display:flex;align-items:center;gap:5px;padding-left:6px;color:var(--white)}
.store i{width:10px;height:10px;border-radius:2px;background:var(--white)}
.footer{left:0;top:973px;width:698px;height:227px;background:var(--footer)}
.footer-base{left:0;top:1146px;width:698px;height:54px;background:var(--footer-base)}
.fcol{top:991px}
.fcol h5{font-size:7.5px;font-weight:500;color:var(--link);margin-bottom:20px}
.fcol ul{list-style:none;font-size:7px;line-height:14px;color:#e3e9f2}
.social{left:76px;top:1122px;display:flex;gap:3px;align-items:center}
.social i{width:14px;height:14px;border-radius:50%;background:#3b90dc}
.social .sq{width:28px;height:10px;border-radius:1px;background:#dde6f0;margin-left:8px}
.legal{left:75px;top:1155px;font-size:7px;line-height:14px;color:#e3e9f2}
.badge{left:463px;top:1159px;width:36px;height:21px;background:#e9e9ee;border:1px solid #c23}
.badge-text{left:503px;top:1161px;font-size:4px;line-height:9px;color:#cfd8e6}
</style>
</head>
<body>
<div class="abs top-band"></div>

<div class="abs brand"><i class="brand-dot"></i><span class="brand-name">Tallow Brisk</span></div>
<div class="abs brand-tag">MONEY EXCHANGE &amp; TRANSFERS</div>
<div class="abs top-links"><span>Contact us</span><span>|</span><i class="lang-box"></i><span>English ▾</span></div>
<div class="abs top-phone">+ 44 (0)20 7946 0321</div>

<nav class="abs main-nav">
  <span>Home</span><span class="sep">|</span><span>Personal</span><span class="sep">|</span><span>Business</span><span class="sep">|</span><span>Market Knowledge</span><span class="sep">|</span><span>Currency Tools</span><span class="sep">|</span><span>Why TallowBrisk</span>
</nav>

<section class="abs hero">
  <div class="abs hero-photo" role="img" aria-label="Businessman in a suit holding a pink piggy bank"></div>
  <div class="abs hero-dots"><i></i><i></i><i></i><i></i></div>
  <form class="abs quote-panel">
    <h2>Request A Currency Quote</h2>
    <div class="field">Full Name</div>
    <div class="field">Company</div>
    <div class="field">Telephone</div>
    <div class="field">E-Mail</div>
    <div class="captcha"><div class="captcha-inner" role="img" aria-label="Verification words challenge"></div></div>
    <div class="quote-btn">Get A Quote</div>
  </form>
</section>

<h3 class="abs section welcome-h">Welcome to Tallow Brisk</h3>
<p class="abs copy welcome-p1">Lorem Ipsum is simply dummy text of the printing and typesetting industry. Lorem Ipsum has been the industry's standard dummy text ever since the 1500s, when an unknown printer took a galley of type and scrambled it to make a type specimen book. It has survived not only five centuries, but also the leap into electronic typesetting, remaining essentially unchanged. It was popularised in the 1960s with the release of Setwell sheets containing Lorem Ipsum passages, and more recently with desktop publishing software like Pagecraft including versions of Lorem Ipsum</p>
<p class="abs copy welcome-p2">Lorem Ipsum is simply dummy text of the printing and typesetting industry. Lorem Ipsum has been the industry's standard dummy text ever since the 1500s, when an unknown printer took a galley of type and scrambled &nbsp;... <a href="#">Read More</a></p>

<div class="abs open-account">
  <svg class="abs" style="left:14px;top:9px" width="24" height="24" viewBox="0 0 24 24"><rect x="2" y="5" width="16" height="16" fill="none" stroke="#fff" stroke-width="2"/><path d="M9 15l2-5 9-9 3 3-9 9z" fill="#fff"/></svg>
  <b>OPEN ACCOUNT</b><small>Authorised by the FSR</small>
</div>

<div class="abs safety">
  <div class="abs safety-strip"></div>
  <svg class="abs" style="left:6px;top:26px" width="26" height="32" viewBox="0 0 26 32"><path d="M6 14V9a7 7 0 0 1 14 0v5" fill="none" stroke="#fff" stroke-width="3"/><rect x="2" y="14" width="22" height="17" fill="#fff"/><rect x="11.5" y="19" width="3" height="7" fill="#7dbb1f"/></svg>
  <h4>Your Safety</h4>
  <ul>
    <li><svg width="9" height="8" viewBox="0 0 9 8"><path d="M1 4l2.5 3L8 1" stroke="#fff" stroke-width="2" fill="none"/></svg>Authorised by the FSR</li>
    <li><svg width="9" height="8" viewBox="0 0 9 8"><path d="M1 4l2.5 3L8 1" stroke="#fff" stroke-width="2" fill="none"/></svg>Your funds held at Harlow Bank</li>
    <li><svg width="9" height="8" viewBox="0 0 9 8"><path d="M1 4l2.5 3L8 1" stroke="#fff" stroke-width="2" fill="none"/></svg>Secure segregated accounts</li>
  </ul>
</div>

<article class="abs card" style="left:76px">
  <h3>Currency Exchange and International Payments</h3>
  <p class="copy">At TallowBrisk we are a foreign currency broker for private and business clients.<br><br>We place our business focus on providing our clients with the most competitive rates for currency exchange and money transfers whilst executing the highest quality of client service.</p>
  <div class="btns"><span class="btn know">Know More <i></i></span><span class="btn how">How It Works <i></i></span></div>
</article>
<article class="abs card" style="left:262px">
  <h3>Personal Currency Exchange</h3>
  <p class="copy" style="margin-top:25px">Whether you are buying or selling overseas property or simply undertaking money transfers abroad, you need to buy the relevant foreign currency and optimise your budget. This is where we can help and offer competitive rates for both currency exchange and money transfers.</p>
  <div class="btns"><span class="btn know">Know More <i></i></span><span class="btn how">How It Works <i></i></span></div>
</article>
<article class="abs card" style="left:448px">
  <h3>Business Currency Exchange</h3>
  <p class="copy" style="margin-top:25px">We help you to minimise your foreign exchange risks on profit and optimise your international payment costs. Use TallowBrisk's expertise to spend less time managing your international payments and devote more time to growing your business.</p>
  <div class="btns" style="left:10px"><span class="btn know">Know More <i></i></span><span class="btn how">How It Works <i></i></span></div>
</article>

<section class="abs news">
  <h3 class="section">Currency News</h3>
  <h4>International Currency Exchange News</h4>
  <div class="date">1st February to 8th February 2013</div>
  <p>Global markets report: Call us on +44 (0)20 7946 0321<br>or email us to info@tallowbrisk.net...</p>
  <h4 style="margin-top:22px">Currency Exchange Report</h4>
  <div class="date">8th February 2013</div>
  <p>Global markets report: Call us on +44 (0)20 7946 0321<br>or email us to info@tallowbrisk.net...</p>
</section>

<h3 class="abs section video-h">Our Intro Video</h3>
<div class="abs video" role="img" aria-label="Night city skyline with light trails, intro video still"></div>
<div class="abs video-bar"></div>
<svg class="abs video-play" width="14" height="12" viewBox="0 0 14 12"><path d="M3 1l9 5-9 5z" fill="#fff"/></svg>
<p class="abs copy video-p">Lorem Ipsum is simply dummy text of the printing and typesetting industry. Lorem Ipsum has been the industry's standard dummy text ever since the 1500s</p>

<aside class="abs download">
  <b>Download</b><small>Tallow Brisk Mobile Application</small>
  <div class="abs phones" role="img" aria-label="Three smartphones showing the mobile app"></div>
  <div class="abs store" style="left:13px;width:75px;background:#222"><i></i>Phone App</div>
  <div class="abs store" style="left:89px;width:76px;background:var(--green)"><i></i>Tablet App</div>
</aside>

<footer>
  <div class="abs footer"></div>
  <div class="abs footer-base"></div>
  <div class="abs fcol" style="left:76px"><h5>Services</h5><ul><li>Open an individual account</li><li>Open a business account</li><li>Other services</li><li>Refer a friend</li><li>Affiliates</li></ul></div>
  <div class="abs fcol" style="left:203px"><h5>Exchange</h5><ul><li>Canadian dollars to US dollars</li><li>Dollar to euros</li><li>Dollar to pound</li><li>Euros to dollars</li><li>Euros to pounds</li><li>Pounds to dollars</li><li>Pounds to euros</li></ul></div>
  <div class="abs fcol" style="left:319px"><h5>Foreign Exchange</h5><ul><li>Best euro rate</li><li>Best exchange rates</li><li>Currency exchange</li><li>Currency news</li></ul></div>
  <div class="abs fcol" style="left:413px"><h5>Currency Tools</h5><ul><li>Calculator exchange rate</li><li>Currency converter</li><li>Currency conversion</li><li>Foreign currency exchange rates</li></ul></div>
  <div class="abs fcol" style="left:540px"><h5>Why Tallow Brisk</h5><ul><li>About us</li><li>Regulatory</li><li>Careers</li><li>Contact us</li></ul></div>
  <div class="abs social"><i></i><i></i><i></i><i></i><i></i><i></i><span class="sq"></span><span class="sq"></span></div>
  <p class="abs legal">Tallow Brisk Ltd. Registered in England Number 8841207-Registered Office: 14 Marlin STREET London E2 7QT.<br>Copyright © Tallow Brisk 2012 Regulatory info | Disclaimer &amp; Privacy | Site Map | Sign In</p>
  <div class="abs badge"></div>
  <p class="abs badge-text">FSR Authorisation Number: 640218<br>Money Laundering Regulation Number: 19304457</p>
</footer>
</body>
</html>
```